Men's enhance supplement package design (square form)

WHAT WE WANT TO TELL BY DESIGN:Male enhancement, enhance Sexual vitality, strong man, get (back) desire forsex, masculinity, booster.This supplement is not like Tolmaxe but want to tell like Tolmaxe by design.

Target Market(s)

Men who over 30 years old and feel lack of sexual desire.

```html
<!DOCTYPE html>
<html lang="en">
<head>
<meta charset="utf-8">
<title>Vigorathon Original Formula – Dietary Supplement for Men</title>
<link rel="stylesheet" href="https://fonts.googleapis.com/css2?family=Montserrat:wght@400;600;700;800&family=Poppins:wght@400;500&display=swap">
<style>
  :root {
    --ink: #0d0d0d;
    --coal: #1c1c1e;
    --graphite: #2e2e30;
    --red: #e51b2b;
    --red-deep: #9c1420;
    --silver: #c9c9c9;
    --grey: #a3a3a3;
    --white: #ffffff;
  }
  * { margin: 0; padding: 0; box-sizing: border-box; }
  html, body {
    width: 822px; height: 1200px; overflow: hidden; background: var(--ink);
  }
  .package {
    position: relative; width: 822px; height: 1200px; overflow: hidden;
    background: linear-gradient(155deg, var(--graphite) 0%, var(--coal) 35%, var(--ink) 75%, #050505 100%);
    font-family: "Montserrat", sans-serif; color: var(--white);
  }
  .package__shapes { position: absolute; inset: 0; }
  .hero-figure {
    position: absolute; left: 340px; top: 277px; width: 418px; height: 722px;
    background: radial-gradient(ellipse at 55% 40%, #c41826 0%, #7a0f18 40%, #1a1a1a 75%, rgba(20,20,20,0) 100%);
    border-radius: 40% 40% 30% 30%;
  }
  .tagline {
    position: absolute; left: 67px; top: 76px;
    font-size: 30px; font-weight: 400; letter-spacing: 0.5px; color: var(--grey);
  }
  .brand-name {
    position: absolute; left: 68px; top: 122px; width: 640px;
    font-size: 74px; font-weight: 800; letter-spacing: 1px; line-height: 1; color: var(--white);
    white-space: nowrap;
  }
  .formula {
    position: absolute; left: 106px; top: 203px;
    font-family: "Poppins", sans-serif; font-size: 36px; font-weight: 400; color: var(--white);
  }
  .ingredients { position: absolute; left: 0; top: 0; list-style: none; }
  .ingredient {
    position: absolute; height: 40px;
    display: flex; align-items: center; padding-left: 30px;
    font-size: 23px; font-weight: 700; color: var(--white);
  }
  .ingredient::before {
    content: ""; position: absolute; inset: 0; z-index: -1;
    background: linear-gradient(90deg, #000 0%, #151515 60%, #3a3a3a 100%);
    transform: skewX(-25deg);
  }
  .ingredient__more { font-weight: 400; margin-left: 7px; }
  .ingredient--kra { left: 47px; top: 996px; width: 280px; }
  .ingredient--tongkat { left: 76px; top: 1048px; width: 280px; }
  .ingredient--bcaa { left: 106px; top: 1100px; width: 275px; }
  .product-type {
    position: absolute; left: 493px; top: 1070px;
    font-size: 24px; font-weight: 700; color: var(--silver); letter-spacing: 0.2px;
  }
  .count {
    position: absolute; left: 489px; top: 1099px;
    font-size: 82px; font-weight: 800; line-height: 1; color: var(--silver); letter-spacing: -3px;
  }
  .audience {
    position: absolute; left: 596px; top: 1110px; width: 148px; height: 32px;
    display: flex; align-items: center; padding-left: 12px;
    font-size: 24px; font-weight: 800; color: var(--white);
  }
  .audience::before {
    content: ""; position: absolute; inset: 0; z-index: -1;
    background: var(--red); transform: skewX(-22deg);
  }
  .unit {
    position: absolute; left: 607px; top: 1144px;
    font-size: 22px; font-weight: 400; color: var(--grey); letter-spacing: 0.5px;
  }
  .front { position: absolute; inset: 0; z-index: 1; }
</style>
</head>
<body>
  <main class="package">
    <svg class="package__shapes" width="822" height="1200" viewBox="0 0 822 1200" aria-hidden="true">
      <defs>
        <linearGradient id="redPanel" x1="0" y1="0" x2="0.6" y2="1">
          <stop offset="0" stop-color="#9c1420"/>
          <stop offset="0.6" stop-color="#e51b2b"/>
          <stop offset="1" stop-color="#f0202f"/>
        </linearGradient>
      </defs>
      <polygon points="0,395 0,1200 412,1200" fill="url(#redPanel)"/>
      <line x1="0" y1="388" x2="418" y2="1200" stroke="#d8d8d8" stroke-width="5"/>
    </svg>

    <div class="hero-figure" role="img" aria-label="Illustration of a caped warrior in a crested helmet striding forward"></div>

    <div class="front">
      <p class="tagline">HIGH QUALITY</p>
      <h1 class="brand-name">VIGORATHON</h1>
      <p class="formula">Original Formula</p>

      <ul class="ingredients">
        <li class="ingredient ingredient--kra">KRA CHAI DAHM</li>
        <li class="ingredient ingredient--tongkat">TONGKAT ALI</li>
        <li class="ingredient ingredient--bcaa">BCAA<span class="ingredient__more">and more</span></li>
      </ul>

      <p class="product-type">DIETARY SUPPLEMENT</p>
      <p class="count">90</p>
      <p class="audience">FOR MEN</p>
      <p class="unit">TABLETS</p>
    </div>
  </main>
</body>
</html>
```